Kerris Odlen Letter Head

log and letter head

would like a modern feminine approch, please see attached the back of my business card

Kerris Odlen Consulting

ABN 81 540 263 918

Address19a Brood Street Brindle Heights 5082 South Australia

Business

```html
<!DOCTYPE html>
<html lang="en">
<head>
<meta charset="utf-8">
<title>Kerris Odlen Consulting – Stationery</title>
<link href="https://fonts.googleapis.com/css2?family=Quattrocento:wght@400&display=swap" rel="stylesheet">
<style>
  :root{
    --brand-red:#e31e24;
    --paper:#ffffff;
    --ink:#222222;
    --backdrop:#e6e7e9;
    --text-font:"Quattrocento", Georgia, serif;
  }
  *{margin:0;padding:0;box-sizing:border-box}
  html,body{width:1200px;height:1001px;overflow:hidden}
  body{background:var(--backdrop);position:relative;font-family:var(--text-font);color:var(--ink)}
  .sheet{position:absolute;background:var(--paper);box-shadow:0 4px 14px rgba(0,0,0,.18);overflow:hidden}
  .sheet svg.wave{position:absolute;left:0;top:0;display:block}
  .brand-name{position:absolute;left:0;right:0;text-align:center;font-family:var(--text-font);font-weight:400;white-space:nowrap}
  .bottom-bar{position:absolute;left:0;right:0;bottom:0;background:var(--brand-red)}
  .details{position:absolute;font-size:9px;line-height:1.6;white-space:nowrap}
  .details.right{text-align:right}

  /* letterhead with red band */
  .letterhead--band{left:50px;top:68px;width:518px;height:669px}
  .letterhead--band .brand-name{top:30px;font-size:28px;color:var(--paper)}
  .letterhead--band .bottom-bar{height:8px}
  .letterhead--band .details.left{left:26px;bottom:20px}
  .letterhead--band .details.right{right:25px;bottom:18px}

  /* letterhead with red lines */
  .letterhead--lines{left:630px;top:150px;width:520px;height:672px}
  .letterhead--lines .brand-name{top:58px;font-size:28px;color:var(--brand-red)}
  .letterhead--lines .bottom-bar{height:8px}
  .letterhead--lines .details.left{left:26px;bottom:22px}
  .letterhead--lines .details.right{right:25px;bottom:30px}

  /* business card */
  .business-card{left:32px;top:760px;width:530px;height:206px}
  .business-card .brand-name{top:24px;font-size:28px;color:var(--paper)}
  .business-card .bottom-bar{height:7px}
  .business-card .details{font-size:13px;line-height:1.6}
  .business-card .details.left{left:26px;top:120px}
  .business-card .details.right{right:22px;top:128px}
</style>
</head>
<body>

<section class="sheet letterhead--band" aria-label="Letterhead">
  <svg class="wave" width="518" height="130" viewBox="0 0 518 130" aria-hidden="true">
    <path d="M0 0H518V112C430 118 330 98 250 86C160 72 70 78 0 100Z" fill="var(--brand-red)"/>
    <path d="M0 88C90 64 200 66 300 84C390 100 460 106 518 100L518 104C450 112 380 104 300 90C200 72 90 72 0 94Z" fill="var(--paper)"/>
  </svg>
  <p class="brand-name">Kerris Odlen Consulting</p>
  <p class="details left">Kerris Odlen Consulting<br>ABN 81 540 263 918</p>
  <p class="details right">Address:<br>27c Tallow Lane Brindle Heights<br>5082 South Australia</p>
  <div class="bottom-bar"></div>
</section>

<section class="sheet letterhead--lines" aria-label="Letterhead">
  <svg class="wave" width="520" height="200" viewBox="0 0 520 200" aria-hidden="true">
    <path d="M0 176C60 150 130 142 200 140C300 138 420 130 520 80L520 90C430 138 320 146 200 148C130 150 70 158 0 186Z" fill="var(--brand-red)"/>
    <path d="M0 160C70 140 150 132 220 130L180 134C110 140 50 152 0 168Z" fill="var(--brand-red)"/>
    <path d="M380 130C440 118 490 100 520 86L520 96C480 112 430 126 380 130Z" fill="var(--brand-red)"/>
  </svg>
  <p class="brand-name">Kerris Odlen Consulting</p>
  <p class="details left">Kerris Odlen Consulting<br>ABN 81 540 263 918</p>
  <p class="details right">Address:<br>27c Tallow Lane Brindle Heights<br>5082 South Australia</p>
  <div class="bottom-bar"></div>
</section>

<section class="sheet business-card" aria-label="Business card">
  <svg class="wave" width="530" height="120" viewBox="0 0 530 120" aria-hidden="true">
    <path d="M0 0H530V104C440 112 340 94 260 84C170 72 80 76 0 96Z" fill="var(--brand-red)"/>
    <path d="M0 82C90 62 200 64 300 80C390 94 470 98 530 92L530 96C460 104 380 98 300 86C200 70 90 70 0 88Z" fill="var(--paper)"/>
  </svg>
  <p class="brand-name">Kerris Odlen Consulting</p>
  <p class="details left">Kerris Odlen Consulting<br>ABN 81 540 263 918</p>
  <p class="details right">Address:<br>27c Tallow Lane Brindle Heights<br>5082 South Australia</p>
  <div class="bottom-bar"></div>
</section>

</body>
</html>
```